PLM - Business Card Design Project

We need a business card based on our logo
Updates

Hi I just upload logo file in AI format Thanks and regards

Target Market(s)

Bank, Big companies, Business owners

Industry/Entity Type

Business

Font styles to use
Sans Serif

```html
<!DOCTYPE html>
<html lang="fr">
<head>
<meta charset="utf-8">
<title>PLM – Carte de visite</title>
<link href="https://fonts.googleapis.com/css2?family=Questrial&family=Bebas+Neue&display=swap" rel="stylesheet">
<style>
  :root {
    --navy: #0b2a4b;
    --slate: #82918f;
    --paper: #ffffff;
    --rule: #7d7d7d;
  }
  html, body {
    margin: 0;
    padding: 0;
    overflow: hidden;
    background: var(--paper);
  }
  .card {
    position: relative;
    width: 1200px;
    height: 675px;
    background: var(--paper);
    overflow: hidden;
  }
  .brand {
    position: absolute;
    left: 0;
    width: 1200px;
    top: 40px;
    text-align: center;
    font-family: "Questrial", sans-serif;
  }
  .brand-name {
    display: block;
    font-size: 292px;
    line-height: 250px;
    color: var(--navy);
    letter-spacing: -4px;
    padding-left: 10px;
  }
  .firm-name {
    display: block;
    margin-top: 0;
    font-size: 38px;
    line-height: 44px;
    color: var(--navy);
  }
  .services {
    display: block;
    font-size: 19px;
    line-height: 24px;
    color: var(--slate);
    padding-left: 70px;
  }
  .divider {
    position: absolute;
    left: 75px;
    top: 374px;
    width: 1050px;
    height: 6px;
  }
  .contact {
    position: absolute;
    left: 0;
    top: 430px;
    width: 1200px;
    margin: 0;
    padding: 0;
    list-style: none;
    text-align: center;
    font-family: "Bebas Neue", sans-serif;
    font-size: 33px;
    color: var(--navy);
  }
  .contact li {
    height: 69px;
    line-height: 52px;
    letter-spacing: 0.42em;
    padding-left: 0.42em;
  }
</style>
</head>
<body>
<div class="card">
  <div class="brand">
    <span class="brand-name">PLM</span>
    <span class="firm-name">Cabinet Perrin Lemoine Martin</span>
    <span class="services">Expertise-comptable • Audit • Conseil</span>
  </div>

  <svg class="divider" viewBox="0 0 1050 6" preserveAspectRatio="none" aria-hidden="true">
    <defs>
      <linearGradient id="rule-fade" x1="0" x2="1" y1="0" y2="0">
        <stop offset="0" stop-color="#7d7d7d" stop-opacity="0"/>
        <stop offset="0.5" stop-color="#7d7d7d" stop-opacity="1"/>
        <stop offset="1" stop-color="#7d7d7d" stop-opacity="0"/>
      </linearGradient>
    </defs>
    <ellipse cx="525" cy="3" rx="525" ry="2.5" fill="url(#rule-fade)"/>
  </svg>

  <ul class="contact">
    <li class="contact-phone">123 456 789</li>
    <li class="contact-web">www.website.com</li>
    <li class="contact-email">email@email.com</li>
  </ul>
</div>
</body>
</html>
```